Bramble Hollow Networks - Electrical

We need flyers for electrical services.
Areas of work include new builds, office fitouts, switchboard upgrades, installation of ceiling fans, powerpoint and downlight upgrades, home theatre and AV systems, all exterior and emergency work. Free quotes
We would like to see designs with the colour Red with a young and modern design. Licence No: 63914K must be included and call Leopold on 0438917062.

Colors
ec1f27

```html
<!DOCTYPE html>
<html lang="en">
<head>
<meta charset="utf-8">
<title>Bramble Hollow Networks – Electrical Flyer</title>
<link rel="stylesheet" href="https://fonts.googleapis.com/css2?family=Montserrat:wght@800&family=Questrial&display=swap">
<style>
  :root {
    --backdrop: #f29077;
    --brand-red: #ec1f27;
    --deep-red: #c8121a;
    --white: #ffffff;
    --ink: #1a1a1a;
    --hero-light: #e6e9ec;
    --hero-mid: #a9b4bd;
    --hero-dark: #6f7a70;
  }
  html, body {
    margin: 0;
    padding: 0;
    width: 1200px;
    height: 871px;
    overflow: hidden;
    background: var(--backdrop);
  }
  .flyer {
    position: absolute;
    left: 310px;
    top: 25px;
    width: 580px;
    height: 820px;
    background: var(--brand-red);
    overflow: hidden;
    box-shadow: 0 18px 40px rgba(90, 30, 20, 0.35);
    font-family: "Questrial", sans-serif;
    color: var(--white);
  }
  .flyer-shapes {
    position: absolute;
    inset: 0;
  }
  .hero-photo {
    position: absolute;
    left: 0;
    top: 0;
    width: 580px;
    height: 400px;
    background: linear-gradient(170deg, var(--hero-light) 0%, var(--hero-mid) 50%, var(--hero-dark) 100%);
  }
  .brand-name {
    position: absolute;
    left: 40px;
    top: 418px;
    margin: 0;
    line-height: 1.05;
    color: var(--white);
  }
  .brand-name-strong {
    display: block;
    font-family: "Montserrat", sans-serif;
    font-weight: 800;
    font-size: 34px;
  }
  .brand-name-light {
    display: block;
    font-family: "Questrial", sans-serif;
    font-weight: 400;
    font-size: 36px;
  }
  .services {
    position: absolute;
    left: 40px;
    top: 510px;
  }
  .services-title {
    margin: 0 0 8px;
    font-size: 25px;
    font-weight: 400;
  }
  .services-list {
    list-style: none;
    margin: 0;
    padding: 0;
    font-size: 14px;
    line-height: 1.55;
  }
  .services-list li {
    display: flex;
    align-items: center;
    gap: 10px;
  }
  .services-list li::before {
    content: "";
    width: 7px;
    height: 7px;
    border-radius: 50%;
    border: 2px solid var(--white);
    flex: none;
  }
  .services-offer {
    margin: 8px 0 0;
    font-size: 15px;
    letter-spacing: 0.3px;
  }
  .job-photo {
    position: absolute;
    left: 390px;
    width: 164px;
    height: 96px;
    border: 5px solid #f4f4f4;
    box-shadow: 0 2px 6px rgba(0,0,0,0.3);
  }
  .job-photo--wiring {
    top: 420px;
    background: linear-gradient(135deg, #e9eef2 0%, #9fb3c6 55%, #4a78aa 100%);
  }
  .job-photo--switchboard {
    top: 545px;
    background: linear-gradient(135deg, #f0f0f0 0%, #b9b3a6 50%, #3d5795 100%);
  }
  .contact-bar {
    position: absolute;
    left: 0;
    bottom: 0;
    width: 580px;
    height: 78px;
    display: flex;
    align-items: center;
    justify-content: center;
    gap: 16px;
    color: var(--ink);
  }
  .contact-phone {
    display: flex;
    align-items: center;
    gap: 10px;
    font-size: 34px;
    letter-spacing: 1px;
  }
  .contact-divider {
    width: 2px;
    height: 44px;
    background: var(--ink);
  }
  .contact-licence {
    font-size: 22px;
  }
</style>
</head>
<body>
  <article class="flyer">
    <div class="hero-photo" role="img" aria-label="Photo of an electrician holding a hard hat beside solar panels"></div>

    <svg class="flyer-shapes" width="580" height="820" viewBox="0 0 580 820" aria-hidden="true">
      <defs>
        <linearGradient id="silver" x1="0" y1="0" x2="1" y2="0">
          <stop offset="0" stop-color="#9a9a9a"/>
          <stop offset="0.35" stop-color="#f4f4f4"/>
          <stop offset="0.6" stop-color="#bdbdbd"/>
          <stop offset="0.8" stop-color="#ffffff"/>
          <stop offset="1" stop-color="#a8a8a8"/>
        </linearGradient>
      </defs>
      <path class="hero-swoosh" d="M0 372 Q300 410 580 250 L580 275 Q300 425 0 392 Z" fill="url(#silver)"/>
      <path class="red-body" d="M0 390 Q300 423 580 273 L580 820 L0 820 Z" fill="#ec1f27"/>
      <path class="red-wave" d="M200 560 Q330 480 470 560 Q340 520 200 600 Z" fill="#c8121a" opacity="0.35"/>
      <path class="contact-band" d="M0 742 L580 742 L580 820 L0 820 Z" fill="url(#silver)"/>
      <path class="contact-band-edge" d="M380 742 L580 700 L580 742 Z" fill="url(#silver)"/>
    </svg>

    <h1 class="brand-name">
      <span class="brand-name-strong">Bramble Hollow</span>
      <span class="brand-name-light">Networks</span>
    </h1>

    <section class="services">
      <h2 class="services-title">Our services</h2>
      <ul class="services-list">
        <li>New builds</li>
        <li>Office fitouts</li>
        <li>Switchboard upgrades</li>
        <li>Installation of ceiling fans</li>
        <li>Powerpoint and downlight upgrades</li>
        <li>Home theatre and av systems</li>
        <li>All exterior and emergency work</li>
      </ul>
      <p class="services-offer">Free quotes · Call Leopold</p>
    </section>

    <div class="job-photo job-photo--wiring" role="img" aria-label="Photo of an electrician working on wiring"></div>
    <div class="job-photo job-photo--switchboard" role="img" aria-label="Photo of an electrician checking a switchboard"></div>

    <footer class="contact-bar">
      <span class="contact-phone">
        <svg width="26" height="26" viewBox="0 0 24 24" aria-hidden="true">
          <path d="M6.6 10.8a15.1 15.1 0 0 0 6.6 6.6l2.2-2.2a1 1 0 0 1 1-.25 11.4 11.4 0 0 0 3.6.57 1 1 0 0 1 1 1V20a1 1 0 0 1-1 1A17 17 0 0 1 3 4a1 1 0 0 1 1-1h3.5a1 1 0 0 1 1 1c0 1.25.2 2.45.57 3.6a1 1 0 0 1-.25 1Z" fill="#1a1a1a"/>
        </svg>
        0438917062
      </span>
      <span class="contact-divider"></span>
      <span class="contact-licence">Licence No: 63914K</span>
    </footer>
  </article>
</body>
</html>
```